dkfarrowplace website

I need a new homepage design for my current website at www.DKFarrowPlace.example. I want someone to look at my current website and develop a more appealing homepage... right now the colors don't blend very well and it needs a facelift

Reason: This has been extended to September 10th

```html
<!DOCTYPE html>
<html lang="en">
<head>
<meta charset="utf-8">
<title>DK Farrow – Home</title>
<link href="https://fonts.googleapis.com/css2?family=Open+Sans:ital,wght@0,400;0,600;0,700;1,400&family=Oleo+Script:wght@400;700&family=Oswald:wght@500;600&display=swap" rel="stylesheet">
<style>
:root{
  --pink:#d81f7f;
  --ink:#4a4a4a;
  --text:#555;
  --muted:#777;
  --page:#f1f1f1;
  --white:#fff;
  --line:#d6d6d6;
  --footer:#4b4b4b;
  --green:#2f7d2a;
  --teal:#1f6f8f;
  --star:#f28b1c;
}
*{box-sizing:border-box;margin:0;padding:0}
html,body{width:828px;height:1200px;overflow:hidden}
body{position:relative;background:var(--page);font-family:"Open Sans",Arial,sans-serif;color:var(--text)}
.abs{position:absolute}
.column{left:90px;top:54px;width:648px;height:1058px;background:var(--white);box-shadow:0 0 4px rgba(0,0,0,.18)}
.topbar{left:0;top:0;width:828px;height:54px;background:linear-gradient(#c81c76,#dc3089 40%,#d0247e);border-top:3px solid #a81262}
.brand{left:90px;top:18px;color:var(--white);font-weight:600;font-size:16px}
.nav{left:240px;top:24px;display:flex;font-size:12.5px;color:var(--white)}
.nav span{margin-right:26px}
.hero{left:97px;top:60px;width:634px;height:328px;background:linear-gradient(100deg,#efe6ea 0%,#f4e9ee 40%,#f0dde5 70%,#e8d3dc 100%);border:1px solid var(--line)}
.hero-photo{left:110px;top:60px;width:170px;height:328px;background:linear-gradient(#e9dce2,#9b8c92 35%,#4a4245 70%,#3b3437)}
.hero-arrow{width:32px;height:32px;border-radius:50%;border:2px solid #c9b9bd;background:rgba(255,255,255,.35)}
.hero-copy{left:300px;top:100px;width:420px;text-align:center}
.h-discover{font-family:"Oleo Script",cursive;font-weight:700;font-style:italic;color:var(--pink);font-size:56px;line-height:60px}
.h-secrets{font-family:"Oleo Script",cursive;font-weight:700;font-style:italic;color:var(--pink);font-size:32px;line-height:28px;margin-top:2px}
.h-big{font-weight:700;color:#3e3e3e;font-size:50px;line-height:50px}
.h-amp{font-weight:700;color:var(--pink);font-size:46px;line-height:30px}
.report{left:97px;top:399px;width:634px;height:122px;background:linear-gradient(#f7f7f7,#e6e6e6);border:1px solid #dcdcdc}
.book{background:linear-gradient(135deg,#d83b3b,#2c6cb0 55%,#f3f3f3)}
.green-book{background:linear-gradient(135deg,#e3f3e8,#6bbf4a 55%,#2e7d3b)}
.report-title{left:199px;top:410px;font-size:12px;color:#333;font-weight:600}
.report-title b{color:var(--pink);font-size:15px;font-weight:600}
.report-sub{left:199px;top:438px;font-size:9px;color:var(--muted)}
.report-sub em{color:var(--pink);font-style:normal}
.field{height:22px;background:var(--white);border:1px solid #d9d9d9;font-size:9px;color:#888;padding:5px 7px}
.btn{left:558px;top:458px;width:85px;height:22px;background:var(--pink);color:var(--white);font-weight:600;font-size:12px;text-align:center;line-height:22px}
.privacy{left:199px;top:494px;font-size:9px;color:var(--muted)}
.privacy em{color:var(--pink);font-style:normal}
.welcome{left:97px;top:545px;width:634px;text-align:center;font-size:15px;font-weight:600;color:#444}
.intro{left:97px;top:574px;width:636px;font-size:8.4px;line-height:17.6px;color:#666}
.product{width:210px;height:104px}
.product .thumb{position:absolute;left:0;top:0;width:80px;height:103px;border:1px solid #e3e3e3;background:var(--white);padding:4px}
.product .thumb div{width:100%;height:100%}
.product .name{position:absolute;left:92px;top:4px;font-size:9.5px;line-height:16px;color:#444;width:118px}
.product .stars{position:absolute;left:92px;top:40px;font-size:9px;color:var(--star);letter-spacing:-1px}
.product .stars small{font-size:5px;color:#999;letter-spacing:0;margin-left:4px}
.product .quote{position:absolute;left:91px;top:62px;font-size:7.5px;line-height:14px;color:#555;width:120px}
.banner{left:96px;top:805px;width:634px;height:186px;background:linear-gradient(90deg,#e2f6d6,#f6fdf0 50%,#def3d0)}
.b-title{left:160px;top:830px;width:290px;font-weight:700;color:var(--green);font-size:38px;line-height:44px}
.b-tag{left:160px;top:940px;font-family:"Oswald",sans-serif;font-weight:500;color:var(--green);font-size:15px}
.b-avail{left:460px;top:941px;color:var(--teal);font-size:12px;font-weight:600}
.b-by{left:227px;top:961px;font-size:10.5px;color:#3c8e9f}
.badge{left:465px;top:840px;width:88px;height:88px;border-radius:50%;background:radial-gradient(circle at 40% 35%,#2a8fb5,#1c6d8e);color:var(--white);font-family:"Oswald",sans-serif;font-weight:500;font-size:11.5px;line-height:14.5px;text-align:center;padding-top:22px}
.banner-book{left:572px;top:815px;width:100px;height:145px;transform:rotate(8deg)}
.press{height:44px;top:1038px;background:var(--white);border:1px solid #ddd;display:flex;align-items:center;justify-content:center;font-weight:700;font-size:11px;color:#333;white-space:nowrap}
.mini-arrow{width:15px;height:15px;border-radius:50%;border:1px solid #bbb;top:1053px;background:var(--white)}
.footer{left:0;top:1112px;width:828px;height:88px;background:var(--footer)}
.f-links{left:89px;top:1130px;font-size:9.5px;color:#eee}
.f-links span{margin:0 7px}
.f-copy{left:91px;top:1155px;font-size:8px;color:#eee}
.social{top:1139px;width:24px;height:24px;border-radius:50%;border:2px solid #f2f2f2}
.f-code{left:782px;top:1165px;font-size:9px;color:#ddd}
</style>
</head>
<body>
<div class="abs column"></div>

<header class="abs topbar"></header>
<div class="abs brand">DK Farrow</div>
<nav class="abs nav"><span>Home</span><span>Products</span><span>About</span><span>Blog</span><span>Forum</span><span>Media Room</span><span>Success Stories</span></nav>

<section class="abs hero"></section>
<div class="abs hero-photo" role="img" aria-label="Portrait photo of the author in a dark dress"></div>
<div class="abs hero-arrow" style="left:78px;top:208px"></div>
<div class="abs hero-arrow" style="left:719px;top:208px"></div>
<div class="abs hero-copy">
  <div class="h-discover">Discover</div>
  <div class="h-secrets">Secrets To A</div>
  <div class="h-big">Alimmer Sexier</div>
  <div class="h-amp">&amp;</div>
  <div class="h-big">Heathier You!</div>
</div>

<section class="abs report"></section>
<div class="abs book" style="left:116px;top:421px;width:56px;height:72px" role="img" aria-label="Cover of the free report book"></div>
<div class="abs report-title"><b>FREE Report:</b>"5 Reasons You Can't Lose Weight!"</div>
<div class="abs report-sub">Just enter your name and email below to get instant access to this 30 page report absolutely <em>FREE!</em></div>
<div class="abs field" style="left:199px;top:458px;width:166px">Name:</div>
<div class="abs field" style="left:376px;top:458px;width:166px">Email:</div>
<div class="abs btn">SUBSCRIBE</div>
<div class="abs privacy"><em>E-mail Privacy:</em> Sign up with complete confidence! We will never sell, rent, lease, or share your information with anyone.</div>

<h2 class="abs welcome">Welcome To Our Site!</h2>
<p class="abs intro">Welcome to Campus, a multipurpose lorem ipsum dolo. Go ahead and click around, tmultipurpose lorem ipsum dolo. Go ahead and click around, tmultipurpose lore adipisicing elit, sed do eiusmod tempor incididunt ut labore et dolore magna aliqua., tmultipurpose lorem ipsum dolo. Go ahead and click around, tmultipurpose lore . Go ahead and click around, there is a ton of new stuff tWelcome to Campus, a multipu, tmultipurpose lorem ipsum dolo. Go ahead and click around, tmultipurpose lo Go ahead and click around, there is a ton of new stuff tWelcom.</p>

<div class="abs product" style="left:96px;top:670px">
  <div class="thumb"><div class="book" role="img" aria-label="Cover of the weight loss report"></div></div>
  <div class="name">5 reasons you ccant loss your weight.</div>
  <div class="stars">★★★★★<small>(86 Reviews)</small></div>
  <div class="quote">Helena Marsh, authorof things are better than a good.</div>
</div>
<div class="abs product" style="left:311px;top:670px">
  <div class="thumb"><div class="green-book" role="img" aria-label="Cover of the green juice reset book"></div></div>
  <div class="name">5 reasons you ccant loss your weight.</div>
  <div class="stars">★★★★★<small>(86 Reviews)</small></div>
  <div class="quote">Helena Marsh, authorof things are better than a good.</div>
</div>
<div class="abs product" style="left:526px;top:670px">
  <div class="thumb"><div class="green-book" role="img" aria-label="Cover of the green juice reset book"></div></div>
  <div class="name">5 reasons you ccant loss your weight.</div>
  <div class="stars">★★★★★<small>(86 Reviews)</small></div>
  <div class="quote">Helena Marsh, authorof things are better than a good.</div>
</div>

<section class="abs banner"></section>
<h3 class="abs b-title">10-Day Green<br>Juice Reset</h3>
<div class="abs b-tag">LOSE WEIGHT. GET HEALTHY. FEEL ENERGIZED.</div>
<div class="abs b-avail">Available Now</div>
<div class="abs b-by">By DK Farrow, #1 Bestselling Author, Nutritionist and Weight-Loss Expert</div>
<div class="abs badge">LOSE UP TO<br>15 POUNDS<br>IN 10 DAYS!</div>
<div class="abs banner-book green-book" role="img" aria-label="Cover of the green juice reset book"></div>

<div class="abs mini-arrow" style="left:79px"></div>
<div class="abs press" style="left:96px;width:96px">Channel Six</div>
<div class="abs press" style="left:205px;width:76px">Westline</div>
<div class="abs press" style="left:294px;width:125px">Orbit Radio</div>
<div class="abs press" style="left:433px;width:50px">Metro 9</div>
<div class="abs press" style="left:496px;width:54px">Wave 98</div>
<div class="abs press" style="left:564px;width:104px">Gleam</div>
<div class="abs press" style="left:676px;width:54px">Wave 98</div>
<div class="abs mini-arrow" style="left:733px"></div>

<footer class="abs footer"></footer>
<div class="abs f-links">Privacy Policy<span>|</span>Terms of Use<span>|</span>Disclaimer</div>
<div class="abs f-copy">Copyright © 2011 Corvane Publishing</div>
<div class="abs social" style="left:593px" aria-label="Social link"></div>
<div class="abs social" style="left:622px" aria-label="Social link"></div>
<div class="abs social" style="left:651px" aria-label="Social link"></div>
<div class="abs social" style="left:679px" aria-label="Social link"></div>
<div class="abs social" style="left:707px" aria-label="Social link"></div>
<div class="abs f-code">C4</div>
</body>
</html>
```